Looking for an Innovative Print Design (Service Directory)

We need a new design for our advertisement within a printed colour services directory.

We are a compensation law firm called Harlow Compensation Lawyers. Feel free to take a browse of our website www.harlowlegalteam.com.au to get an idea of what we do and the kind of firm we are.

We are in the process of redeveloping our website and as such, so please don't adhere to the design principles of the current site- impress us with your originality!

On top of any editable formats, your final submissions must include a .pdf copy.
The same design will need to be presented in two dimensions:

- 154mm x 118mm (B1/B2 Half Page);
- 175mm x 113mm (B4 Half Page).

[For more information refer to attached Pdf.]

We have attached for you a few examples of other firms' designs (Sample1,2,3). These are by no means good, or what we're after, it's just to provide you with an idea of what sort of advertisements go into the service directory.

Hi all,

We want to emphasise that a priority of the design is that it must look:
• Professional
• Sophisticated
Please do not hesitate to use completely different colour schemes to the ones that are on our website- as we have said, our website will change in the near future, so cohesion between the current project and the website is not necessary!

Thanks!

Thank you for your submissions so far. There are some great ideas hidden in there. 

An issue we are having is that most of you are conforming to the same understanding of what it should look like. Remember that there is NO NEED to be bound by the image of firm as is. That is, feel free to use a different colour logo.

For inspiration, we relate well to the design aesthetics of: http://www.quillstudio.co.uk/

Look forward to seeing your 'out of the box' submissions. 

Reason: We've received a large amount of fantastic designs. However, what we're really looking for is something original. Please feel free to think outside the box (the final design doesn't need to look like a print ad), and construct a design that is completely incongruous with our website! While we do appreciate a minimalistic design, we have yet to receive something that really grabs your attention with its visuals. We're not sure but this may or may not be achieved with a full colour design. Thanks for all your submissions- they all have some features that really click with us. We look forward to the next wave of submissions!

Target Market(s)

We have various target markets, including mainly families, elderly people, blue collar workers.

These are individuals who are looking for assistance. They feel helpless or wronged.

Keep in mind that the people accessing these are those who prefer going to a printed directory rather than using a google search.

Industry/Entity Type

Law Firm

Font styles to use
Serif
Sans Serif

Requirements
Must have
• - Our name 'Harlow Compensation Lawyers'
- Our logo (attached as logo.eps, logo.png, and logo.tif)
- Must include phone number as 1300 XXX XXX (this must be prominent)
- Must include the following service areas in these words: Motor vehicle claims, medical claims, superannuation claims, Workplace claims, negligence claims
- Our email address: info@harlowlegalteam.com.au
- Our website address: www.harlowlegalteam.com.au
- The following catchphrases: '98% success rate', and 'No win no fee' in those words
- Our location '482 Penrose Lane, Smithville, SYDNEY'
- For sizing dimensions, we need one in 154mm x 118mm and also a design in 175mm x 113mm (B4 Half Page) [refer to pdf attached]
Nice to have
• - Text indicating free initial consulatation
- Professional colour scheme
- As our website will be changed, do not worry about making the advertisement cohesive with our website design
- We want the design to be modern, but still professional
- Clean typeface
- No gradient colour scheme
- When designing, if you are looking to place more text onto the advertisement, these may be some considerations (feel free to change the wording): Accredited specialists, home and hospital visits

```html
<!DOCTYPE html>
<html lang="en">
<head>
<meta charset="utf-8">
<title>Harlow Compensation Lawyers – Directory Advertisements</title>
<link rel="stylesheet" href="https://fonts.googleapis.com/css2?family=Roboto:wght@300;400;500;700&display=swap">
<style>
  :root {
    --board: #1e1e1e;
    --blue: #1b84b6;
    --orange: #f26b21;
    --ink: #333333;
    --ink-soft: #454545;
    --white: #ffffff;
    --photo-a: #c9d3da;
    --photo-b: #4a4f58;
  }
  * { margin: 0; padding: 0; box-sizing: border-box; }
  html, body { width: 1200px; height: 1000px; overflow: hidden; }
  body {
    position: relative;
    background: var(--board);
    font-family: "Roboto", Arial, sans-serif;
  }
  .size-label {
    position: absolute;
    color: var(--white);
    font-size: 44px;
    font-weight: 400;
    transform: translateY(-50%);
    white-space: nowrap;
  }
  .ad {
    position: absolute;
    background: var(--white);
    overflow: hidden;
  }
  .ad--half-b1 { left: 300px; top: 33px; width: 602px; height: 463px; }
  .ad--half-b4 { left: 250px; top: 523px; width: 690px; height: 449px; }
  .ad__shapes { position: absolute; inset: 0; width: 100%; height: 100%; }
  .ad__el {
    position: absolute;
    transform: translateY(-50%);
    white-space: nowrap;
    line-height: 1;
  }
  .ad__el--right { text-align: right; }

  .brand { display: flex; align-items: center; gap: 12px; color: var(--white); font-weight: 300; }
  .brand__dot { width: 48px; height: 48px; border-radius: 50%; background: var(--orange); flex: none; }
  .brand__name { font-size: 31px; letter-spacing: 1px; line-height: 1; }
  .brand__sub { font-size: 9px; letter-spacing: 1.6px; margin-top: 3px; }

  .phone { color: var(--white); font-weight: 700; font-size: 34px; letter-spacing: 1.5px; }

  .services__title { color: var(--blue); font-weight: 700; font-size: 26px; }
  .services__item { display: flex; align-items: center; gap: 8px; color: var(--ink); font-weight: 700; font-size: 16.5px; }
  .bullet { width: 17px; height: 17px; border-radius: 50%; border: 4px solid var(--orange); flex: none; }

  .contact { display: flex; align-items: center; gap: 6px; font-size: 11px; color: var(--ink); }
  .contact--web { color: var(--white); font-size: 12px; }

  .firm-name { color: var(--orange); font-weight: 700; font-size: 38px; }
  .firm-tagline { color: var(--ink-soft); font-size: 16px; }
  .claim { color: var(--blue); font-weight: 700; font-size: 30px; }
  .claim__accent { color: var(--orange); }
  .claim__big { font-size: 1.12em; }
  .claim--fee { font-size: 28px; }

  .address { color: var(--white); font-size: 14px; line-height: 1.45; }
  .address__street { font-weight: 700; }

  .photo {
    position: absolute;
    background: linear-gradient(110deg, var(--photo-a) 0%, #e4e9ec 40%, var(--photo-b) 100%);
  }
  .ad--half-b4 .firm-name { font-size: 40px; }
  .ad--half-b4 .claim { font-size: 31px; }
  .ad--half-b4 .claim--fee { font-size: 29px; }
</style>
</head>
<body>

<span class="size-label" style="left:82px; top:412px;">154x 118</span>
<span class="size-label" style="left:960px; top:872px;">175x 113</span>

<section class="ad ad--half-b1" aria-label="Harlow Compensation Lawyers advertisement, 154 by 118">
  <svg class="ad__shapes" viewBox="0 0 602 463" preserveAspectRatio="none" aria-hidden="true">
    <path d="M0 0 H602 V64 H330 L310 85 H0 Z" fill="var(--blue)"/>
    <path d="M333 67 H602 V84 H316 Z" fill="var(--orange)"/>
    <rect x="0" y="119" width="32" height="25" fill="var(--orange)"/>
    <rect x="572" y="122" width="30" height="23" fill="var(--blue)"/>
    <path d="M0 407 H305 L285 423 H0 Z" fill="var(--blue)"/>
    <path d="M0 426 H286 L309 405 H602 V463 H0 Z" fill="var(--orange)"/>
  </svg>

  <div class="ad__el brand" style="left:34px; top:47px;">
    <span class="brand__dot"></span>
    <span><span class="brand__name">HARLOW</span><br><span class="brand__sub">COMPENSATION LAWYERS</span></span>
  </div>
  <div class="ad__el ad__el--right phone" style="right:30px; top:40px;">1300 482 910</div>

  <div class="ad__el services__title" style="left:38px; top:132px;">Our Service</div>
  <div class="ad__el services__item" style="left:35px; top:167px;"><span class="bullet"></span>Motor vehicle claims</div>
  <div class="ad__el services__item" style="left:35px; top:211px;"><span class="bullet"></span>Medical claims</div>
  <div class="ad__el services__item" style="left:35px; top:255px;"><span class="bullet"></span>Superannuation claims</div>
  <div class="ad__el services__item" style="left:35px; top:299px;"><span class="bullet"></span>Workplace claims</div>
  <div class="ad__el services__item" style="left:35px; top:343px;"><span class="bullet"></span>Negligence claims</div>
  <div class="ad__el contact" style="left:35px; top:387px;">
    <svg width="16" height="11" viewBox="0 0 16 11" aria-hidden="true"><rect x="0.75" y="0.75" width="14.5" height="9.5" fill="none" stroke="var(--orange)" stroke-width="1.5"/><path d="M1 1 L8 6.5 L15 1" fill="none" stroke="var(--orange)" stroke-width="1.5"/></svg>
    info@harlowlegalteam.com.au
  </div>

  <div class="ad__el ad__el--right firm-name" style="right:32px; top:133px;">Harlow</div>
  <div class="ad__el ad__el--right firm-tagline" style="right:32px; top:167px;">Compensation Lawyers</div>
  <div class="ad__el ad__el--right claim" style="right:30px; top:198px;"><span class="claim__accent claim__big">98%</span> success rate</div>
  <div class="ad__el ad__el--right claim claim--fee" style="right:30px; top:240px;">No <span class="claim__accent">win no</span> fee</div>

  <div class="photo" role="img" aria-label="Photo of a lawyer meeting with a client" style="left:368px; top:284px; width:202px; height:106px;"></div>

  <div class="ad__el contact contact--web" style="left:35px; top:444px;">
    <svg width="16" height="16" viewBox="0 0 16 16" aria-hidden="true"><g fill="none" stroke="var(--white)" stroke-width="1.3"><circle cx="8" cy="8" r="7"/><ellipse cx="8" cy="8" rx="3" ry="7"/><path d="M1 8 H15"/></g></svg>
    www.harlowlegalteam.com.au
  </div>
  <div class="ad__el ad__el--right address" style="right:32px; top:435px;">
    <span class="address__street">482 Penrose Lane</span><br>Smithville, SYDNEY
  </div>
</section>

<section class="ad ad--half-b4" aria-label="Harlow Compensation Lawyers advertisement, 175 by 113">
  <svg class="ad__shapes" viewBox="0 0 690 449" preserveAspectRatio="none" aria-hidden="true">
    <path d="M0 0 H690 V69 H390 L370 88 H0 Z" fill="var(--blue)"/>
    <path d="M393 71 H690 V87 H376 Z" fill="var(--orange)"/>
    <rect x="0" y="122" width="35" height="25" fill="var(--orange)"/>
    <rect x="660" y="124" width="30" height="32" fill="var(--blue)"/>
    <path d="M0 393 H330 L312 411 H0 Z" fill="var(--blue)"/>
    <path d="M0 413 H312 L334 392 H690 V449 H0 Z" fill="var(--orange)"/>
  </svg>

  <div class="ad__el brand" style="left:36px; top:49px;">
    <span class="brand__dot"></span>
    <span><span class="brand__name">HARLOW</span><br><span class="brand__sub">COMPENSATION LAWYERS</span></span>
  </div>
  <div class="ad__el ad__el--right phone" style="right:30px; top:42px;">1300 482 910</div>

  <div class="ad__el services__title" style="left:40px; top:134px;">Our Service</div>
  <div class="ad__el services__item" style="left:38px; top:170px;"><span class="bullet"></span>Motor vehicle claims</div>
  <div class="ad__el services__item" style="left:38px; top:212px;"><span class="bullet"></span>Medical claims</div>
  <div class="ad__el services__item" style="left:38px; top:254px;"><span class="bullet"></span>Superannuation claims</div>
  <div class="ad__el services__item" style="left:38px; top:296px;"><span class="bullet"></span>Workplace claims</div>
  <div class="ad__el services__item" style="left:38px; top:338px;"><span class="bullet"></span>Negligence claims</div>
  <div class="ad__el contact" style="left:38px; top:377px;">
    <svg width="16" height="11" viewBox="0 0 16 11" aria-hidden="true"><rect x="0.75" y="0.75" width="14.5" height="9.5" fill="none" stroke="var(--orange)" stroke-width="1.5"/><path d="M1 1 L8 6.5 L15 1" fill="none" stroke="var(--orange)" stroke-width="1.5"/></svg>
    info@harlowlegalteam.com.au
  </div>

  <div class="ad__el ad__el--right firm-name" style="right:32px; top:137px;">Harlow</div>
  <div class="ad__el ad__el--right firm-tagline" style="right:32px; top:170px;">Compensation Lawyers</div>
  <div class="ad__el ad__el--right claim" style="right:30px; top:204px;"><span class="claim__accent claim__big">98%</span> success rate</div>
  <div class="ad__el ad__el--right claim claim--fee" style="right:30px; top:244px;">No <span class="claim__accent">win no</span> fee</div>

  <div class="photo" role="img" aria-label="Photo of a lawyer meeting with a client" style="left:455px; top:274px; width:203px; height:108px;"></div>

  <div class="ad__el contact contact--web" style="left:38px; top:429px;">
    <svg width="16" height="16" viewBox="0 0 16 16" aria-hidden="true"><g fill="none" stroke="var(--white)" stroke-width="1.3"><circle cx="8" cy="8" r="7"/><ellipse cx="8" cy="8" rx="3" ry="7"/><path d="M1 8 H15"/></g></svg>
    www.harlowlegalteam.com.au
  </div>
  <div class="ad__el ad__el--right address" style="right:32px; top:420px;">
    <span class="address__street">482 Penrose Lane</span><br>Smithville, SYDNEY
  </div>
</section>

</body>
</html>
```